Excelente custo beneficio !!! Já utilizei a KPF, para diversos serviços, como logo, cardápio, flyer, arte para cavalete e, o principal, é que sempre fico satisfeito com o resultado final. Agora falta só o site..rsrs

```html
<!DOCTYPE html>
<html lang="pt-BR">
<head>
<meta charset="utf-8">
<title>Maré Alta — Flyer</title>
<link rel="stylesheet" href="https://fonts.googleapis.com/css2?family=Kaushan+Script&family=Open+Sans:wght@400;600;700&display=swap">
<style>
  :root {
    --page-bg: #ece9e4;
    --paper: #ffffff;
    --ink: #1b1b1b;
    --body-ink: #3a3a3a;
    --navy: #1d2a6b;
    --blue: #2b4fb3;
    --red: #d42a2a;
    --orange: #f08a24;
    --yellow: #f7c23a;
    --accent-line: #b0283c;
    --photo-frame: #ffffff;
    --dark-frame: #2a2a2a;
  }
  * { margin: 0; padding: 0; box-sizing: border-box; }
  html, body { width: 1200px; height: 1200px; overflow: hidden; }
  body { background: var(--page-bg); font-family: "Open Sans", Arial, sans-serif; }

  .canvas { position: relative; width: 1200px; height: 1200px; overflow: hidden; }

  .flyer {
    position: absolute; left: 200px; top: 20px;
    width: 800px; height: 1160px;
    background: var(--paper);
    box-shadow: 0 4px 18px rgba(0,0,0,.18);
    overflow: hidden;
  }

  .color-bars { position: absolute; left: 25px; top: 0; width: 100px; height: 96px; }

  .hibiscus-small {
    position: absolute; left: 212px; top: 58px; width: 42px; height: 42px;
    border-radius: 50%; background: radial-gradient(circle, #f25a3c, var(--red));
  }

  .headline {
    position: absolute; left: 80px; top: 112px; width: 440px;
    font-family: "Kaushan Script", cursive;
    font-weight: 400;
    font-size: 58px; line-height: 1.38; color: var(--ink);
  }

  .intro { position: absolute; left: 83px; top: 280px; width: 390px; color: var(--body-ink); }
  .intro p { font-size: 12.5px; line-height: 1.45; text-align: justify; margin-bottom: 14px; }
  .intro .lead { display: block; font-weight: 700; letter-spacing: 2.6px; text-align: justify; }

  .divider {
    position: absolute; left: 260px; top: 516px; width: 215px; height: 3px;
    background: linear-gradient(90deg, rgba(176,40,60,0), var(--accent-line) 30%, var(--accent-line));
  }

  .photo {
    position: absolute; border: 6px solid var(--photo-frame);
    box-shadow: 0 3px 10px rgba(0,0,0,.25);
  }
  .photo-plate { left: 530px; top: 36px; width: 265px; height: 228px;
    background: linear-gradient(135deg, #f1ede6, #c9b79a 45%, #c8702f 75%, #7a5a3a); }
  .photo-drinks { left: 530px; top: 288px; width: 265px; height: 216px;
    background: linear-gradient(180deg, #9bb2c9, #d9753a 45%, #f29a3a 65%, #7d7f86); }

  .photo-platter {
    position: absolute; left: 83px; top: 542px; width: 460px; height: 504px;
    background: linear-gradient(160deg, #6b4a2e, #b98a58 35%, #d9b27a 55%, #8a5b35 80%, #4a3422);
  }

  .swirls {
    position: absolute; left: 390px; top: 530px; width: 410px; height: 340px;
    background: radial-gradient(ellipse at 60% 40%, rgba(247,194,58,.9), rgba(240,138,36,.7) 35%, rgba(212,42,90,.5) 60%, rgba(43,79,179,.35) 80%, rgba(255,255,255,0) 100%);
  }

  .brand { position: absolute; left: 210px; top: 745px; width: 360px; height: 290px; text-align: center; }
  .brand-disc {
    width: 200px; height: 200px; margin: 0 auto;
    border-radius: 50%;
    background: linear-gradient(180deg, #f7a24a, #e9603a);
  }
  .brand-name {
    margin-top: 6px;
    font-family: "Kaushan Script", cursive;
    font-size: 58px; line-height: 1; color: var(--ink);
  }

  .foliage {
    position: absolute; left: 0; top: 770px; width: 205px; height: 312px;
    background: linear-gradient(160deg, #f6f1e4 0%, #6fa35a 40%, #2f6d3a 75%, #1f4a28 100%);
    border-top-right-radius: 120px;
  }
  .hibiscus-large {
    position: absolute; left: 140px; top: 950px; width: 84px; height: 84px;
    border-radius: 50%; background: radial-gradient(circle, #f36a4a, var(--red) 70%);
  }

  .photo-bowl {
    position: absolute; left: 558px; top: 870px; width: 232px; height: 178px;
    border: 5px solid var(--dark-frame);
    background: radial-gradient(circle at 50% 50%, #e8b86a, #c2612e 40%, #2d5aa0 65%, #3a2e24 100%);
  }

  .contact-note {
    position: absolute; left: 558px; top: 1052px;
    font-size: 10px; line-height: 1.2; color: var(--body-ink);
  }

  .footer-band {
    position: absolute; left: 0; bottom: 0; width: 800px; height: 78px;
    background: linear-gradient(90deg, var(--yellow) 0%, var(--orange) 22%, var(--red) 45%, #7a2a6a 65%, var(--navy) 100%);
    color: #fff;
  }
  .footer-city { position: absolute; right: 40px; top: 10px; font-size: 13px; font-weight: 600; }
  .footer-address { position: absolute; right: 40px; bottom: 14px; font-size: 14px; }
</style>
</head>
<body>
<div class="canvas">
  <article class="flyer">
    <svg class="color-bars" viewBox="0 0 100 96" aria-hidden="true">
      <defs>
        <linearGradient id="barBlue" x1="0" y1="1" x2="0" y2="0">
          <stop offset="0" stop-color="#1d2a6b"/><stop offset="1" stop-color="#ffffff"/>
        </linearGradient>
        <linearGradient id="barWarm" x1="0" y1="1" x2="0" y2="0">
          <stop offset="0" stop-color="#d42a2a"/><stop offset=".6" stop-color="#f08a24"/><stop offset="1" stop-color="#f7c23a"/>
        </linearGradient>
      </defs>
      <rect x="0" y="26" width="34" height="70" fill="url(#barBlue)"/>
      <rect x="52" y="0" width="30" height="90" fill="url(#barWarm)"/>
    </svg>

    <div class="hibiscus-small" role="img" aria-label="Flor de hibisco vermelha"></div>

    <h1 class="headline">venha saborear<br>nossas delícias !</h1>

    <div class="intro">
      <p><span class="lead">Lorem ipsum dolor sit amet, consectetur adipiscing elit,</span>
      sed do eiusmod tempor incididunt ut labore et dolore magna aliqua. Ut enim ad minim veniam, quis nostrud exercitation ullamco laboris nisi ut aliquip ex ea commodo consequat.</p>
      <p><span class="lead">Lorem ipsum dolor sit amet, consectetur adipiscing elit,</span>
      sed do eiusmod tempor incididunt ut labore et dolore magna aliqua. Ut enim ad minim veniam, quis nostrud exercitation ullamco laboris nisi ut aliquip ex ea commodo consequat.</p>
    </div>

    <div class="divider"></div>

    <div class="photo photo-plate" role="img" aria-label="Foto de prato com salada e frango empanado"></div>
    <div class="photo photo-drinks" role="img" aria-label="Foto de drinks alaranjados em taças ao ar livre"></div>

    <div class="photo-platter" role="img" aria-label="Foto de tábua de petiscos variados sobre madeira"></div>
    <div class="swirls" role="img" aria-label="Ilustração de ondas coloridas em tons de amarelo, laranja, rosa e azul"></div>

    <div class="foliage" role="img" aria-label="Ilustração de folhas tropicais e flores brancas"></div>
    <div class="hibiscus-large" role="img" aria-label="Flor de hibisco vermelha"></div>

    <div class="brand">
      <div class="brand-disc"></div>
      <div class="brand-name">Maré Alta</div>
    </div>

    <div class="photo-bowl" role="img" aria-label="Foto de tigela com petiscos fritos e frutas"></div>

    <div class="contact-note">Ligue já<br>Peça online</div>

    <footer class="footer-band">
      <div class="footer-city">RIO DE JANEIRO / RJ</div>
      <div class="footer-address">R. Endereço, numero – Bairro, cidade – SP 00000-000</div>
    </footer>
  </article>
</div>
</body>
</html>
```